Re-design Company presentation for LumoVerityNet

The current presentation has the right content, but we need to make serious changes in terms of colors, backgrounds, etc.
You can view the current state of the PPT as a skeleton that needs to be revamped to make it look professional & visually appealing.
Please feel free to make any changes as necessary, but please maintain text editable and consider that we might add for example new individual client logos in the future, so generally avoid large chunks of images combined together.
If you require any specific logos in a better format, or if you have any questions at all, please feel free to ask.

```html
<!DOCTYPE html>
<html lang="en">
<head>
<meta charset="utf-8">
<title>LumoVerityNet – Company Presentation</title>
<link href="https://fonts.googleapis.com/css2?family=Barlow:wght@400;500;600;700&family=Roboto:wght@400;500;700&display=swap" rel="stylesheet">
<style>
:root{
  --canvas:#c4c4c4;
  --orange:#ee6a4a;
  --orange-deep:#e2583a;
  --navy:#2b3242;
  --blue:#3b5b8c;
  --blue-soft:#3d5a80;
  --night:#061028;
  --ink:#2b3242;
  --muted:#6b7280;
  --white:#ffffff;
}
*{margin:0;padding:0;box-sizing:border-box}
html,body{width:1200px;height:1072px;overflow:hidden;background:var(--canvas)}
body{position:relative;font-family:'Roboto',sans-serif;color:var(--ink)}
.slide{position:absolute;width:544px;height:306px;background:var(--white);overflow:hidden}
.col-left{left:38px}.col-right{left:618px}
.row-1{top:45px}.row-2{top:380px}.row-3{top:720px}
.abs{position:absolute}

/* shared slide furniture */
.slide-marker{position:absolute;left:-2px;top:21px;width:11px;height:11px;background:var(--orange);transform:rotate(45deg);border-radius:2px}
.slide-title{position:absolute;left:38px;top:16px;font-family:'Barlow',sans-serif;font-weight:600;font-size:14px;color:var(--ink)}
.slide-lead{position:absolute;left:270px;top:19px;width:240px;font-size:6.6px;line-height:1.3;color:var(--ink)}
.footer{position:absolute;left:0;bottom:0;width:100%;height:28px;background:var(--navy);color:var(--white)}
.footer-brand{position:absolute;left:19px;top:8px;font-family:'Barlow',sans-serif;font-size:10px;letter-spacing:.2px;display:flex;align-items:center;gap:5px}
.footer-brand .mark{width:7px;height:7px;background:var(--orange)}
.footer-copy{position:absolute;left:0;right:0;top:11px;text-align:center;font-size:4.6px}
.footer-page{position:absolute;right:14px;top:11px;font-size:4.6px}

/* title slide */
.cover{background:var(--night)}
.cover-backdrop{position:absolute;inset:0;background:radial-gradient(ellipse at 70% 30%,#1b3556 0%,#0b1a36 45%,#050c20 100%)}
.shape{position:absolute;transform:rotate(45deg)}
.shape.blue{background:var(--blue-soft)}
.shape.orange{background:var(--orange)}
.cover-brand{position:absolute;left:0;right:0;top:134px;text-align:center;font-family:'Barlow',sans-serif;color:var(--white);font-size:12px;display:flex;justify-content:center;align-items:center;gap:5px}
.cover-brand .mark{width:8px;height:8px;background:var(--orange)}
.cover-title{position:absolute;left:0;right:0;top:154px;text-align:center;font-family:'Barlow',sans-serif;font-weight:700;font-size:21px;color:var(--white)}
.cover-rule{position:absolute;left:137px;top:185px;width:270px;height:1px;background:var(--orange)}
.cover-sub{position:absolute;left:0;right:0;top:191px;text-align:center;font-family:'Barlow',sans-serif;font-weight:600;font-size:11.5px;line-height:14px;color:var(--white)}
.line{position:absolute}
.line.o{background:var(--orange)}.line.b{background:var(--blue-soft)}

/* services */
.service{position:absolute;top:53px;width:115px;height:174px;background:var(--white);box-shadow:0 2px 8px rgba(0,0,0,.08)}
.service-frame{position:absolute;top:49px;width:119px;height:182px;border:4px solid var(--orange);border-radius:3px}
.service-frame.top{border-bottom:none;height:30px}
.service-frame.bottom{top:201px;border-top:none;height:30px}
.service-icon{position:absolute;left:12px;top:16px;width:40px;height:40px;border-radius:50%;background:var(--orange);display:flex;align-items:center;justify-content:center}
.service-name{position:absolute;left:14px;top:63px;width:95px;font-family:'Barlow',sans-serif;font-weight:600;font-size:8.4px;line-height:11px}
.service-text{position:absolute;left:14px;top:89px;width:89px;font-size:4.7px;line-height:8.5px;color:var(--muted);text-align:justify}

/* vision */
.vision-card{position:absolute;left:38px;width:225px;height:55px;background:var(--white);box-shadow:0 1px 6px rgba(0,0,0,.09)}
.vision-num{position:absolute;left:9px;top:7px;font-family:'Barlow',sans-serif;font-weight:700;font-size:20px;color:var(--orange)}
.vision-text{position:absolute;left:36px;top:9px;width:181px;font-size:5.6px;line-height:8.5px;color:var(--muted)}
.vision-accent{position:absolute;left:292px;top:79px;width:3px;height:147px;background:var(--orange)}
.vision-photo{position:absolute;left:297px;top:0;width:247px;height:278px;background:linear-gradient(160deg,#9aa4ad 0%,#5e6a74 45%,#3a3f45 100%)}

/* deliverables */
.deliv{position:absolute;top:50px;width:146px;height:177px;background:var(--white);box-shadow:0 1px 7px rgba(0,0,0,.09)}
.deliv-photo{position:absolute;left:7px;top:6px;width:132px;height:76px}
.deliv-name{position:absolute;left:17px;top:86px;font-family:'Barlow',sans-serif;font-weight:600;font-size:10px}
.deliv-list{position:absolute;left:17px;top:104px;width:122px;list-style:none}
.deliv-list li{position:relative;padding-left:9px;font-size:5.7px;line-height:8.5px;color:var(--muted);margin-bottom:8px}
.deliv-list li svg{position:absolute;left:0;top:1.5px}

/* clients */
.client{position:absolute;width:78px;height:78px}
.client .tile{position:absolute;left:11px;top:11px;width:56px;height:56px;background:var(--white);border-radius:10px;transform:rotate(45deg);box-shadow:0 4px 10px rgba(0,0,0,.09)}
.client .name{position:absolute;inset:0;display:flex;align-items:center;justify-content:center;font-family:'Barlow',sans-serif;font-weight:600;font-size:9px;color:var(--ink);text-align:center}

/* problems */
.stat{position:absolute;width:162px;height:162px}
.stat .tile{position:absolute;left:24px;top:24px;width:114px;height:114px;border-radius:18px;transform:rotate(45deg)}
.stat.blue .tile{background:linear-gradient(135deg,#3f62a0,#2f4c80)}
.stat.orange .tile{background:linear-gradient(135deg,#f06c46,#d8502f)}
.stat .value{position:absolute;left:0;right:0;top:46px;text-align:center;font-family:'Barlow',sans-serif;font-weight:700;font-size:24px;color:var(--white)}
.stat .caption{position:absolute;left:36px;right:36px;top:80px;text-align:center;font-size:6.6px;line-height:8.5px;color:var(--white)}
</style>
</head>
<body>

<!-- Cover -->
<section class="slide col-left row-1 cover">
  <div class="cover-backdrop" role="img" aria-label="Dark blue financial data chart backdrop"></div>
  <div class="shape blue" style="left:-45px;top:-40px;width:90px;height:90px;border-radius:14px"></div>
  <div class="shape orange" style="left:-22px;top:69px;width:40px;height:40px;border-radius:8px"></div>
  <div class="shape orange" style="left:520px;top:170px;width:55px;height:55px;border-radius:10px"></div>
  <div class="shape blue" style="left:500px;top:240px;width:120px;height:120px;border-radius:18px"></div>
  <div class="line o" style="left:110px;top:76px;width:66px;height:2px"></div>
  <div class="line b" style="left:110px;top:76px;width:2px;height:65px"></div>
  <div class="line o" style="left:372px;top:247px;width:66px;height:2px"></div>
  <div class="line b" style="left:436px;top:184px;width:2px;height:65px"></div>
  <div class="cover-brand"><span class="mark"></span>LumoVerityNet</div>
  <h1 class="cover-title">Tagging Data You Can Trust</h1>
  <div class="cover-rule"></div>
  <p class="cover-sub">Proposal Created for LumoVerityNet by<br>Dorin Vasile &amp; Owen Hartley Jan 20,2024</p>
</section>

<!-- Services -->
<section class="slide col-right row-1">
  <span class="slide-marker"></span>
  <h2 class="slide-title">Our Services</h2>

  <div class="service-frame bottom" style="left:34px"></div>
  <div class="service-frame top" style="left:154px"></div>
  <div class="service-frame bottom" style="left:274px"></div>
  <div class="service-frame top" style="left:394px"></div>

  <article class="service" style="left:36px">
    <div class="service-icon"><svg width="20" height="20" viewBox="0 0 20 20" fill="#fff"><rect x="2" y="11" width="3" height="7"/><rect x="7" y="8" width="3" height="10"/><rect x="12" y="10" width="3" height="8"/><rect x="17" y="5" width="2" height="13"/><path d="M2 8 L8 4 L13 7 L18 2" stroke="#fff" stroke-width="1.5" fill="none"/></svg></div>
    <h3 class="service-name">Analytics<br>Implementation</h3>
    <p class="service-text">We help you deploy analytics and measurement capabilities. Providing you with data and tagging expertise to create an effective reporting framework. We are specialists in data compliance, data privacy and consent management</p>
  </article>
  <article class="service" style="left:156px">
    <div class="service-icon"><svg width="20" height="20" viewBox="0 0 20 20"><circle cx="10" cy="10" r="6.5" fill="none" stroke="#fff" stroke-width="3" stroke-dasharray="3 2"/><circle cx="10" cy="10" r="4" fill="#fff"/></svg></div>
    <h3 class="service-name">Data Strategy</h3>
    <p class="service-text" style="top:78px">Starting from requirements gathering &amp; auditing your current set-up, to solution architecture &amp; continuous development plans, our team has the capability to take your project from its idea stages, to a fully-fledged business solution that can be used to expand your business.</p>
  </article>
  <article class="service" style="left:276px">
    <div class="service-icon"><svg width="20" height="20" viewBox="0 0 20 20" fill="none" stroke="#fff" stroke-width="1.8"><rect x="5" y="5" width="10" height="10" rx="2"/><path d="M8 2v3M12 2v3M8 15v3M12 15v3M2 8h3M2 12h3M15 8h3M15 12h3"/></svg></div>
    <h3 class="service-name">Advanced<br>Technologies</h3>
    <p class="service-text">We partner with visionary customers who want to transform and grow their organization by building their business using modern digital marketing technologies. We develop custom data models to help you track revenue against marketing spend.</p>
  </article>
  <article class="service" style="left:396px">
    <div class="service-icon"><svg width="20" height="20" viewBox="0 0 20 20" fill="#fff"><rect x="8" y="2" width="4" height="6"/><rect x="3" y="6" width="4" height="2"/><rect x="13" y="6" width="4" height="2"/><path d="M2 10h16v2a8 6 0 0 1-16 0z"/></svg></div>
    <h3 class="service-name">Continuous<br>Improvement</h3>
    <p class="service-text">All our solutions are designed to include multiple fail-safes. Our code &amp; configurations are engineered to be robust and to allow future development. We include automated testing tools that can help our clients maintain high Data Quality standards at all times.</p>
  </article>

  <footer class="footer"><div class="footer-brand"><span class="mark"></span>LumoVerityNet</div><div class="footer-copy">© Copyright 2024 Company name. All Rights Reserved.</div><div class="footer-page">PAGE NO : 04</div></footer>
</section>

<!-- Vision -->
<section class="slide col-left row-2">
  <span class="slide-marker"></span>
  <h2 class="slide-title">Our Vision</h2>
  <div class="vision-card" style="top:47px"><span class="vision-num">01</span><p class="vision-text">We understand the importance of data-driven decisions in organisations of all sizes. If the data collected from your website / app is incorrect, or incomplete, then the outcome of your decisions is invariably a reflection of that.</p></div>
  <div class="vision-card" style="top:109px"><span class="vision-num">02</span><p class="vision-text">This is why our analytics implementation work is not only carefully vetted on multiple layers, but the implementation itself is engineered to include multiple fail-safes designed with data quality in mind.</p></div>
  <div class="vision-card" style="top:172px"><span class="vision-num">03</span><p class="vision-text">We thrive by making our customers understand the value of trusted data, fueling them with confidence to make bold business decisions.</p></div>
  <div class="vision-accent"></div>
  <div class="vision-photo" role="img" aria-label="Photo of a business team meeting around a round table in a city office"></div>
  <footer class="footer"><div class="footer-brand"><span class="mark"></span>LumoVerityNet</div><div class="footer-copy">© Copyright 2024 Company name. All Rights Reserved.</div><div class="footer-page" style="right:14px;left:auto">PAGE NO : 02</div></footer>
</section>

<!-- Deliverables -->
<section class="slide col-right row-2">
  <span class="slide-marker"></span>
  <h2 class="slide-title">Key Deliverables</h2>
  <p class="slide-lead">Implementations are tested both manually &amp; with automated tools to make sure your data can always be trusted</p>

  <article class="deliv" style="left:39px">
    <div class="deliv-photo" role="img" aria-label="Photo of a team planning at a whiteboard" style="background:linear-gradient(135deg,#c9b79c,#7d6a55)"></div>
    <h3 class="deliv-name">Data strategy</h3>
    <ul class="deliv-list">
      <li><svg width="6" height="6" viewBox="0 0 6 6"><circle cx="3" cy="3" r="3" fill="#ee6a4a"/><path d="M1.6 3.1l1 1 1.8-2" stroke="#fff" stroke-width=".8" fill="none"/></svg>Gather requirements to obtain clear objectives</li>
      <li><svg width="6" height="6" viewBox="0 0 6 6"><circle cx="3" cy="3" r="3" fill="#ee6a4a"/><path d="M1.6 3.1l1 1 1.8-2" stroke="#fff" stroke-width=".8" fill="none"/></svg>Deep dives on key analytics platforms</li>
      <li><svg width="6" height="6" viewBox="0 0 6 6"><circle cx="3" cy="3" r="3" fill="#ee6a4a"/><path d="M1.6 3.1l1 1 1.8-2" stroke="#fff" stroke-width=".8" fill="none"/></svg>Recommended roadmap</li>
    </ul>
  </article>
  <article class="deliv" style="left:200px">
    <div class="deliv-photo" role="img" aria-label="Photo of colleagues reviewing charts on a desk" style="background:linear-gradient(135deg,#4a6584,#1f2f45)"></div>
    <h3 class="deliv-name">Tracking implementation</h3>
    <ul class="deliv-list">
      <li><svg width="6" height="6" viewBox="0 0 6 6"><circle cx="3" cy="3" r="3" fill="#ee6a4a"/><path d="M1.6 3.1l1 1 1.8-2" stroke="#fff" stroke-width=".8" fill="none"/></svg>Technology-agnostic Tag Management System setup</li>
      <li><svg width="6" height="6" viewBox="0 0 6 6"><circle cx="3" cy="3" r="3" fill="#ee6a4a"/><path d="M1.6 3.1l1 1 1.8-2" stroke="#fff" stroke-width=".8" fill="none"/></svg>Analytics solution implementation</li>
      <li><svg width="6" height="6" viewBox="0 0 6 6"><circle cx="3" cy="3" r="3" fill="#ee6a4a"/><path d="M1.6 3.1l1 1 1.8-2" stroke="#fff" stroke-width=".8" fill="none"/></svg>Customer Data Platforms Implementation</li>
    </ul>
  </article>
  <article class="deliv" style="left:361px">
    <div class="deliv-photo" role="img" aria-label="Photo of hands pointing at printed charts" style="background:linear-gradient(135deg,#2d4a6e,#8a6a3c)"></div>
    <h3 class="deliv-name">Analytics compliance</h3>
    <ul class="deliv-list">
      <li><svg width="6" height="6" viewBox="0 0 6 6"><circle cx="3" cy="3" r="3" fill="#ee6a4a"/><path d="M1.6 3.1l1 1 1.8-2" stroke="#fff" stroke-width=".8" fill="none"/></svg>Consent Management Platform integrations</li>
      <li style="margin-bottom:0"><svg width="6" height="6" viewBox="0 0 6 6"><circle cx="3" cy="3" r="3" fill="#ee6a4a"/><path d="M1.6 3.1l1 1 1.8-2" stroke="#fff" stroke-width=".8" fill="none"/></svg>Align cookie and other tracking tech with local laws</li>
      <li><svg width="6" height="6" viewBox="0 0 6 6"><circle cx="3" cy="3" r="3" fill="#ee6a4a"/><path d="M1.6 3.1l1 1 1.8-2" stroke="#fff" stroke-width=".8" fill="none"/></svg>Navigate evolving data privacy requirements</li>
    </ul>
  </article>

  <footer class="footer"><div class="footer-brand"><span class="mark"></span>LumoVerityNet</div><div class="footer-copy">© Copyright 2024 Company name. All Rights Reserved.</div><div class="footer-page">PAGE NO : 05</div></footer>
</section>

<!-- Clients -->
<section class="slide col-left row-3">
  <span class="slide-marker"></span>
  <h2 class="slide-title">Clients We Work With</h2>
  <div class="client" style="left:71px;top:59px"><div class="tile"></div><div class="name">Sproutline</div></div>
  <div class="client" style="left:163px;top:59px"><div class="tile"></div><div class="name">Velorent</div></div>
  <div class="client" style="left:257px;top:59px"><div class="tile"></div><div class="name">Ledgerhall</div></div>
  <div class="client" style="left:350px;top:59px"><div class="tile"></div><div class="name">Quietnest<br>Stays</div></div>
  <div class="client" style="left:118px;top:131px"><div class="tile"></div><div class="name">Roamguide</div></div>
  <div class="client" style="left:211px;top:131px"><div class="tile"></div><div class="name">Pactwise</div></div>
  <div class="client" style="left:304px;top:131px"><div class="tile"></div><div class="name">Monoprism</div></div>
  <div class="client" style="left:397px;top:131px"><div class="tile"></div><div class="name">Checkfield</div></div>
  <footer class="footer"><div class="footer-brand"><span class="mark"></span>LumoVerityNet</div><div class="footer-copy">© Copyright 2024 Company name. All Rights Reserved.</div><div class="footer-page">PAGE NO : 03</div></footer>
</section>

<!-- Problems -->
<section class="slide col-right row-3">
  <span class="slide-marker"></span>
  <h2 class="slide-title">Data Related Problems</h2>
  <p class="slide-lead">Companies are struggling with data tagging, consent, privacy compliance and the ability to measure return on marketing spend</p>
  <div class="stat blue" style="left:37px;top:61px"><div class="tile"></div><div class="value">85%</div><p class="caption">of business are not fully confident in their consent management and privacy compliance strategy</p></div>
  <div class="stat orange" style="left:191px;top:61px"><div class="tile"></div><div class="value">76%</div><p class="caption">of businesses don't understand traffic sources or unable to visualize revenue against marketing sources</p></div>
  <div class="stat blue" style="left:346px;top:61px"><div class="tile"></div><div class="value">74%</div><p class="caption">of businesses don't have a universal data tagging governance in place</p></div>
  <footer class="footer"><div class="footer-brand"><span class="mark"></span>LumoVerityNet</div><div class="footer-copy">© Copyright 2024 Company name. All Rights Reserved.</div><div class="footer-page">PAGE NO : 06</div></footer>
</section>

</body>
</html>
```